Postcard Design

We need a postcard to send to prospective clients. We are a debt collection law firm that works exclusively within the state of Nevada. We are committed to collecting debts while being completely compliant with all applicable laws (FDCPA, QLM, HVJN, etc.) We have a call center and are able to tailor our efforts to the specific needs of individual clients and have been in business for over 10 years. We can provide skip tracing through our internal skip tracing department and can file lawsuits in any Justice or District Court within the State of Nevada. We provide pre and post judgment remedies as well as enforce foreign judgments. We work exclusively throughout the State of Nevada. We can levy bank accounts, wages and in many instances file liens on personal property to efficiently liquidate your receivables. We can work with car dealerships, property management companies, banks and other financial institutions or anybody who is owed money by past or present customers.

```html
<!DOCTYPE html>
<html lang="en">
<head>
<meta charset="utf-8">
<title>Daniel M. Ostrander, P.C. — Postcard</title>
<link href="https://fonts.googleapis.com/css2?family=Cinzel:wght@400;700&family=Arimo:wght@700&display=swap" rel="stylesheet">
<style>
  :root {
    --wood-dark: #7a3d1f;
    --wood-mid: #a35a2e;
    --wood-light: #b86b3a;
    --panel: #c3c3c3;
    --panel-edge: #ffffff;
    --ink: #7d1414;
    --title: #efe3d6;
    --notice-bg: #c9c9c9;
    --notice-ink: #e01414;
    --accent-a: #ffa446;
    --accent-b: #f28a22;
    --gavel-a: #3a2516;
    --gavel-b: #a87a52;
    --badge: #9da6b3;
  }
  html, body { margin: 0; padding: 0; overflow: hidden; }
  .postcard {
    position: relative; width: 1200px; height: 930px; overflow: hidden;
    background: radial-gradient(ellipse at 50% 45%, var(--wood-light) 0%, var(--wood-mid) 50%, var(--wood-dark) 100%);
    font-family: "Cinzel", serif; font-weight: 700; color: var(--ink);
  }
  .firm-name {
    position: absolute; top: 78px; left: 0; width: 1200px; margin: 0;
    text-align: center; font-size: 60px; font-weight: 700; letter-spacing: 1px;
    color: var(--title); text-shadow: 3px 4px 6px rgba(0,0,0,.55);
  }
  .panel {
    position: absolute; top: 190px; height: 472px; width: 353px;
    background: var(--panel); border: 3px solid var(--panel-edge); border-radius: 4px;
    box-shadow: 4px 6px 14px rgba(0,0,0,.5); box-sizing: border-box;
  }
  .panel > * { position: absolute; margin: 0; }
  .panel--contact { left: 52px; }
  .panel--services { left: 425px; }
  .panel--membership { left: 795px; width: 354px; }

  .icon { display: block; }
  .icon--pin { left: 12px; top: 72px; }
  .icon--phone { left: 10px; top: 122px; }
  .icon--mail { left: 11px; top: 178px; }
  .contact-text { left: 65px; font-size: 14px; line-height: 20px; white-space: nowrap; }
  .contact-text--address { top: 68px; }
  .contact-text--phone { top: 145px; }
  .contact-text--email { left: 69px; top: 191px; font-size: 12px; }

  .milestone-year {
    left: 2px; font-size: 40px; line-height: 40px; font-weight: 700; letter-spacing: -2px;
    transform: scaleX(.62); transform-origin: left center; white-space: nowrap;
  }
  .milestone-rule { left: 61px; width: 2px; background: var(--ink); }
  .milestone-text { left: 67px; font-size: 13.5px; line-height: 18px; white-space: nowrap; }
  .milestone-year--1 { top: 255px; }
  .milestone-rule--1 { top: 250px; height: 28px; }
  .milestone-text--1 { top: 249px; }
  .milestone-year--2 { top: 317px; }
  .milestone-rule--2 { top: 320px; height: 18px; }
  .milestone-text--2 { top: 319px; }
  .milestone-year--3 { top: 367px; }
  .milestone-rule--3 { top: 369px; height: 18px; }
  .milestone-text--3 { top: 367px; }

  .services-text { left: 0; width: 100%; text-align: center; white-space: nowrap; }
  .services-lead { top: 29px; font-size: 13.5px; line-height: 19.5px; }
  .services-mission { top: 121px; font-size: 13.5px; line-height: 18.5px; }
  .services-detail { font-size: 9px; line-height: 12.2px; }
  .services-detail--clients { top: 230px; }
  .services-detail--courts { top: 279px; }
  .callout {
    top: 369px; left: 20px; width: 327px; height: 42px; box-sizing: border-box;
    background: linear-gradient(var(--accent-a), var(--accent-b)); box-shadow: 2px 3px 5px rgba(0,0,0,.35);
    font-size: 9px; line-height: 12px; text-align: right; padding: 3px 4px 0 0; white-space: nowrap;
  }

  .hero-image {
    top: 0; left: 0; width: 348px; height: 223px;
    background: linear-gradient(135deg, var(--gavel-a) 0%, var(--gavel-b) 55%, #cfae88 100%);
  }
  .member-heading { top: 226px; left: 0; width: 100%; text-align: center; font-size: 30px; line-height: 36px; }
  .partner-name { top: 278px; left: 22px; width: 170px; font-size: 21px; line-height: 25px; }
  .partner-badge { top: 267px; left: 202px; width: 130px; height: 85px; background: var(--badge); border-radius: 3px; }
  .license-note { top: 374px; left: 0; width: 100%; text-align: center; font-size: 13.5px; line-height: 20px; white-space: nowrap; }

  .notice {
    position: absolute; top: 764px; left: 207px; width: 784px; height: 54px;
    background: var(--notice-bg); display: flex; align-items: center; justify-content: center;
    font-family: "Arimo", sans-serif; font-weight: 700; font-size: 36px; color: var(--notice-ink);
    text-shadow: 2px 2px 3px rgba(0,0,0,.45); letter-spacing: .5px;
  }
</style>
</head>
<body>
<div class="postcard">
  <h1 class="firm-name">DANIEL M. OSTRANDER, P.C.</h1>

  <section class="panel panel--contact">
    <svg class="icon icon--pin" width="32" height="44" viewBox="0 0 34 46" aria-hidden="true"><path d="M17 2C8.7 2 2 8.7 2 17c0 11 15 27 15 27s15-16 15-27C32 8.7 25.3 2 17 2z" fill="var(--ink)"/><circle cx="17" cy="16" r="6" fill="var(--panel)"/></svg>
    <p class="contact-text contact-text--address">LOCATED AT 4150 W. CORAL AVE.<br>SUITE 310 LAS VEGAS<br>NEVADA 89117</p>
    <svg class="icon icon--phone" width="38" height="42" viewBox="0 0 40 44" aria-hidden="true"><path d="M9 2l7 9-4 5c3 6 7 11 13 14l5-4 8 7-5 8C17 40 3 24 2 9z" fill="var(--ink)"/></svg>
    <p class="contact-text contact-text--phone">702-555-0148</p>
    <svg class="icon icon--mail" width="46" height="30" viewBox="0 0 46 32" aria-hidden="true"><rect x="1" y="1" width="44" height="30" fill="var(--ink)"/><path d="M2 2l21 16L44 2M2 30l16-14M44 30L28 16" stroke="var(--panel)" stroke-width="2" fill="none"/></svg>
    <p class="contact-text contact-text--email">New_Inquiries@Ostranderlaw.com</p>

    <span class="milestone-year milestone-year--1">1998</span>
    <span class="milestone-rule milestone-rule--1"></span>
    <p class="milestone-text milestone-text--1">COMPLETED HIS LEGAL EDUCATION<br>AT THE HARROW VALLEY SCHOOL<br>OF LAW</p>
    <span class="milestone-year milestone-year--2">1999</span>
    <span class="milestone-rule milestone-rule--2"></span>
    <p class="milestone-text milestone-text--2">ADMITTED TO THE DISTRICT OF<br>COLUMBIA BAR</p>
    <span class="milestone-year milestone-year--3">2003</span>
    <span class="milestone-rule milestone-rule--3"></span>
    <p class="milestone-text milestone-text--3">ADMITTED TO THE STATE BAR<br>OF NEVADA</p>
  </section>

  <section class="panel panel--services">
    <p class="services-text services-lead">DANIEL M. OSTRANDER, ESQ.<br>SPECIALIZES HIS PRACTICE TO THE<br>COLLECTION OF DEBTS AND THE<br>ENFORCEMENT OF JUDGMENTS</p>
    <p class="services-text services-mission">DEDICATED TO THE ETHICAL AND<br>COMPLIANT COLLECTION OF DEBTS AND<br>SUBSEQUENT ENFORCEMENT OF JUDGMENTS<br>THAT WORKS EXCLUSIVELY THROUGHOUT<br>THE STATE OF NEVADA.</p>
    <p class="services-text services-detail services-detail--clients">WE REPRESENT FINANCIAL INSTITUTIONS, PROPERTY MANAGEMENT<br>FIRMS, AUTOMOBILE DEALERSHIPS AND CAN HELP ANYBODY<br>WHO WOULD LIKE TO LIQUIDATE THEIR ACCOUNTS RECEIVABLES</p>
    <p class="services-text services-detail services-detail--courts">WE CAN FILE CLAIMS IN ANY JUSTICE AND DISTRICT COURT<br>THROUGHOUT THE STATE OF NEVADA AND PRIDE OURSELVES<br>ON EFFICIENT AND EFFECTIVE ENFORCEMENT OF JUDGMENTS<br>THROUGH ANY LAWFUL MEANS INCLUDING LIENS, WAGE<br>AND BANK GARNISHMENTS.</p>
    <div class="callout">WE HAVE A CALL CENTER AND PROVIDE PRE-LITIGATION<br>COLLECTION EFFORTS INCLUDING COMPREHENSIVE<br>SKIP-TRACING AND EMPLOYMENT SEARCHES.</div>
  </section>

  <section class="panel panel--membership">
    <div class="hero-image" role="img" aria-label="Photo of a wooden judge's gavel on its block in front of law books"></div>
    <h2 class="member-heading">MEMBER</h2>
    <p class="partner-name">CRESTLINE<br>ALLIANCE</p>
    <div class="partner-badge" role="img" aria-label="Professional association membership badge"></div>
    <p class="license-note">LICENSED TO PRACTICE LAW IN NEVADA<br>AND THE DISTRICT OF COLUMBIA</p>
  </section>

  <div class="notice">NOTICE: THIS IS AN ADVERTISEMENT</div>
</div>
</body>
</html>
```